Personal Business Card

Looking for a clean and modern personal business card. Basically I need something catchy to give to potential clients and people I meet. I do a lot of freelancing (from DJ'ing to wedding videography, but its mostly on the event side of things) so it's more-so about selling myself rather than identifying with a company. I'm starting to meet more people that I want to work with after meeting them so I'm revamping my business cards.

I'm looking for a clean and modern design- I know that's really vague but I'm fine with anything ranging from a symbol to just a fancy version of my name.

Details I need on the front:
Dennis Kowal
dennis@denniskowal-mail.net
(555) 807-2291

On the back I'd like to have something simple like "Nice to have met you today" or "Great meeting you".

UPDATE 9/27 Noon: My apologies for not putting it up before- I'm definitely looking for full color. Doesn't have to be a rainbow but I am looking for the least amount of blank white as possible.

UPDATE 10/1: Really impressed with what I've been getting so far and I'm working on giving everyone feedback- if your design is still up then you're still in the run. Looking for something more unique and modern so please do not post something that looks like a template from Cardloom!

Target Market(s)

Mainly to give to people aged 18-35. Most of my encounters will be casual so the card should have a "young" feeling to it. I rarely do anything in the corporate world so it doesn't have to be boring. It should give the impression that I'm the one they should go to if they need what I do (again it changes every weekend so I'll probably say the "what I do" part.

Industry/Entity Type

Wedding

Requirements
Must have
• Basically the contact information listed above
Nice to have
• I really like the colors Blue, Silver, and Purple. They don't have to necessarily all be there though. I do like the look of polished metal if that makes sense.
Should not have
• A template that resembles card-loom. I'm in a point in my life where I'm working a lot of different markets/areas so the card does not need to have an address or address placeholder.

```html
<!DOCTYPE html>
<html lang="en">
<head>
<meta charset="utf-8">
<title>Dennis Kowal — Business Cards</title>
<link rel="stylesheet" href="https://fonts.googleapis.com/css2?family=Amatic+SC:wght@700&display=swap">
<style>
  :root {
    --page: #ffffff;
    --card-blue: #5060ad;
    --card-dark: #231f20;
    --accent-yellow: #f3ec19;
    --text-light: #ffffff;
  }
  * { margin: 0; padding: 0; box-sizing: border-box; }
  html, body {
    width: 1200px;
    height: 1000px;
    overflow: hidden;
    background: var(--page);
  }
  .sheet {
    position: relative;
    width: 1200px;
    height: 1000px;
    font-family: "Amatic SC", cursive;
    font-weight: 700;
  }
  .card {
    position: absolute;
    width: 468px;
    height: 267px;
    display: flex;
    flex-direction: column;
    align-items: center;
    justify-content: center;
    text-align: center;
  }
  .card--blue { background: var(--card-blue); }
  .card--dark { background: var(--card-dark); }
  .card--front-left  { left: 85px;  top: 204px; }
  .card--front-right { left: 647px; top: 204px; }
  .card--back-left   { left: 85px;  top: 527px; }
  .card--back-right  { left: 647px; top: 527px; }

  .card__front-content { margin-top: -4px; }
  .card__name {
    color: var(--accent-yellow);
    font-size: 50px;
    line-height: 1;
    margin-bottom: 2px;
  }
  .card__line {
    color: var(--text-light);
    font-size: 27px;
    line-height: 33px;
  }
  .card__greeting {
    color: var(--accent-yellow);
    font-size: 42px;
    line-height: 1;
    margin-top: -6px;
  }
</style>
</head>
<body>
  <main class="sheet">
    <section class="card card--blue card--front-left">
      <div class="card__front-content">
        <h1 class="card__name">I'm dennis kowal</h1>
        <p class="card__line">i'm here to help you!</p>
        <p class="card__line">shoot me an email at dennis@denniskowal-mail.net</p>
        <p class="card__line">or give me a call at (555) 807-2291</p>
      </div>
    </section>

    <section class="card card--dark card--front-right">
      <div class="card__front-content">
        <h2 class="card__name">I'm dennis kowal</h2>
        <p class="card__line">i'm here to help you!</p>
        <p class="card__line">shoot me an email at dennis@denniskowal-mail.net</p>
        <p class="card__line">or give me a call at (555) 807-2291</p>
      </div>
    </section>

    <section class="card card--blue card--back-left">
      <p class="card__greeting">It was a plasure meeting you!</p>
    </section>

    <section class="card card--dark card--back-right">
      <p class="card__greeting">It was a plasure meeting you!</p>
    </section>
  </main>
</body>
</html>
```